Tincture bottle labels

I need my labels slightly adjusted to replace the ingredients part with the supplement facts as shown in the 3 Fernhollow labels attached, for the other 2 it will have to be copied and add an BQC disclosure on the label as well possibly below the storage info near the bottom of the label

Target Market(s)

Everyone

Industry/Entity Type

Vitamins & Supplements

Requirements
Must have
• Supplement facts box and info for each product and BQC disclosures

```html
<!DOCTYPE html>
<html lang="en">
<head>
<meta charset="utf-8">
<title>Fernhollow Lion's Mane Liquid Drops Label</title>
<link rel="stylesheet" href="https://fonts.googleapis.com/css2?family=Lilita+One&family=Open+Sans:wght@400;600;700&family=Poppins:ital,wght@0,700;1,800&display=swap">
<style>
:root{
  --orange:#f7922a;
  --orange-deep:#ef6a24;
  --green:#3fae49;
  --brick:#a0462a;
  --mortar:#7a2f1b;
  --ink:#111;
  --paper:#fff;
  --photo-dark:#3c3a38;
  --photo-light:#e9dfcf;
}
*{margin:0;padding:0;box-sizing:border-box}
html,body{width:1200px;height:1000px;overflow:hidden;background:var(--paper)}
.canvas{position:relative;width:1200px;height:1000px}
.label{position:absolute;left:0;top:273px;width:1200px;height:454px;overflow:hidden}
.label-bg{position:absolute;inset:0}
.maker{position:absolute;left:44px;top:50px;writing-mode:vertical-rl;font:600 11px/1.25 "Open Sans",sans-serif;color:var(--paper);white-space:pre}
.maker b{font-weight:800}
.site{position:absolute;left:62px;top:178px;writing-mode:vertical-rl;font:400 11px "Open Sans",sans-serif;color:var(--paper)}
.panel{position:absolute;background:var(--paper);border:4px solid var(--ink);border-radius:18px;box-shadow:-6px 6px 0 var(--ink)}
.facts{left:107px;top:45px;width:208px;height:342px;padding:6px 8px;font-family:"Open Sans",sans-serif;color:var(--ink)}
.facts h2{font:400 19px/1 "Lilita One",sans-serif;letter-spacing:.3px}
.facts .meta{font-size:9.5px;line-height:1.35;border-bottom:3px solid var(--ink);padding-bottom:3px;margin-top:2px}
.facts .row{display:flex;justify-content:space-between;font-size:9.5px;font-weight:700;padding:4px 0 3px;border-bottom:1px solid var(--ink)}
.facts .ing{font-size:9.5px;line-height:1.3;padding:3px 0 4px;border-bottom:2px solid var(--ink)}
.facts .dv{font-size:9.5px;padding:3px 0 0}
.facts h3{font:400 15px/1 "Lilita One",sans-serif;text-align:center;margin-top:8px}
.facts p.use{font-size:9.5px;line-height:1.3;text-align:center;margin-top:3px}
.disclaimer{border:1px solid var(--ink);font-size:8.4px;line-height:1.28;text-align:center;padding:3px 4px;margin-top:7px}
.benefits{left:913px;top:43px;width:222px;height:344px;padding:22px 14px 0 18px;color:var(--ink)}
.benefits h2{font:400 21px/1.3 "Lilita One",sans-serif;text-align:center;letter-spacing:.5px}
.benefits h3{font:400 18px/1 "Lilita One",sans-serif;text-align:center;margin-top:18px}
.benefits ul{list-style:none;margin-top:8px}
.benefits li{position:relative;padding-left:15px;font:italic 800 16px/1.12 "Poppins",sans-serif;margin-bottom:10px}
.benefits li::before{content:"";position:absolute;left:0;top:13px;width:6px;height:6px;border-radius:50%;background:var(--ink)}
.brand{position:absolute;left:0;width:1200px;top:170px;text-align:center}
.brand-name{display:inline-flex;align-items:center;gap:10px;font:400 50px/1 "Lilita One",sans-serif;color:var(--green)}
.brand-name i{width:26px;height:26px;border-radius:50%;background:var(--green);display:inline-block}
.product{position:absolute;left:0;width:1200px;top:255px;text-align:center;font:400 40px/1 "Lilita One",sans-serif;color:var(--paper);-webkit-text-stroke:2px var(--ink);paint-order:stroke fill;letter-spacing:1px}
.format{position:absolute;left:490px;top:330px;width:220px;height:54px;border-radius:27px;background:var(--green);color:var(--paper);font:400 19px/54px "Open Sans",sans-serif;text-align:center}
.volume{position:absolute;left:0;width:1200px;top:406px;text-align:center;font:700 17px "Poppins",sans-serif;color:var(--paper);letter-spacing:1px}
</style>
</head>
<body>
<div class="canvas">
  <section class="label">
    <svg class="label-bg" width="1200" height="454" viewBox="0 0 1200 454">
      <defs>
        <linearGradient id="photoTone" x1="0" x2="1" y1="0" y2="0">
          <stop offset="0" stop-color="var(--photo-dark)"/>
          <stop offset=".55" stop-color="var(--photo-light)"/>
          <stop offset="1" stop-color="var(--photo-dark)"/>
        </linearGradient>
        <radialGradient id="orangeGlow" cx=".45" cy=".6" r=".7">
          <stop offset="0" stop-color="var(--orange-deep)"/>
          <stop offset="1" stop-color="var(--orange)"/>
        </radialGradient>
      </defs>
      <rect role="img" aria-label="Photo of lion's mane mushroom growing on wood" x="0" y="0" width="1200" height="145" fill="url(#photoTone)"/>
      <path d="M0 25 H300 C430 25 520 142 660 142 H1200 V454 H0 Z" fill="url(#orangeGlow)"/>
      <rect x="0" y="353" width="1200" height="5" fill="var(--green)"/>
      <rect role="img" aria-label="Brick wall pattern" x="0" y="358" width="1200" height="96" fill="var(--brick)"/>
    </svg>

    <p class="maker"><b>MANUFACTURED BY:</b>
Fernhollow LLC
Brookfield, Ohio</p>
    <p class="site">fernhollow.shop</p>

    <div class="panel facts">
      <h2>SUPLEMENT FACTS</h2>
      <p class="meta">Serving Size: 2 droppers ( 2mL)<br>Servings Per Container : About 30</p>
      <div class="row"><span>AMOUNT PER SERVING</span><span>2mL*</span></div>
      <p class="ing">Organic Lion´s Mane (Hericium Erinaceus), fruitbody extract</p>
      <p class="dv">Daily value not establised</p>
      <h3>SUGGESTED USE:</h3>
      <p class="use">Take 1-2 ml daily or as directed by your healthcare provider. Consume directly or add to beverages for a cognitive boost.</p>
      <h3>STORAGE:</h3>
      <p class="use">Store in a cool, dry place away from sunlight.</p>
      <p class="disclaimer">These statements have not been evaluated by the BQC. This product is not intended to diagnose, treat, cure or prevent any disease.</p>
    </div>

    <div class="brand"><span class="brand-name"><i></i>FERNHOLLOW</span></div>
    <h1 class="product">LION’S MANE</h1>
    <div class="format">LIQUID DROPS</div>
    <p class="volume">2 fl. oz / (60 ml)</p>

    <div class="panel benefits">
      <h2>ENHANCE<br>MEMORY, FOCUS,<br>&amp; NERVE HEALTH</h2>
      <h3>KEY BENEFITS:</h3>
      <ul>
        <li>SUPPORTS BRAIN HEALTH</li>
        <li>COGNITIVE FUNCTION</li>
        <li>NERVE REGENERATION</li>
      </ul>
    </div>
  </section>
</div>
</body>
</html>
```